Safety poster

I need a safety poster. The poster will be a picture of myself. I am wearing a prosthetic arm. In the hook is a "Lock out tag" I promote safety in the workplace. I am a motivational safety speaker. I want to leave posters after I have talked with companies- but also use these posters as advertisement. So- besides the safety slogan, my information needs to be on there too. (Contact info so someone would know how to get me for a speaking engagement)
I have made a few on my own and they are very popular. I think they could be done much better by a professional.
Some slogans:
Lock out complacency
Choose safety
100% preventable
If you don't think it will happen to you...think again
etc....
These posters are usually hung in workplace environments- break rooms and sometimes safety manager offices.
I like my photo in black and white with the "Lock out tag" in red.
I would also like some in full color.
The size will be 11X17 or something like that- they don't need to be very big- but big enough to be seen.
Information at bottom right of poster would say:
Book a Safety Presentation
with Dara Voss
612-555-0487
www.daravossmail.net
Target Market(s)
Manufacturing, hourly workers, salaried workers, safety management
Industry/Entity Type
Safety
Look and feel
Each slider illustrates characteristics of the customer's brand and the style your logo design should communicate.

```html
<!DOCTYPE html>
<html lang="en">
<head>
<meta charset="utf-8">
<title>Safety Poster – Dara Voss</title>
<link rel="stylesheet" href="https://fonts.googleapis.com/css2?family=Anton&family=Roboto+Condensed:ital,wght@1,700;1,800&display=swap">
<style>
  :root {
    --bg-edge: #262626;
    --bg-mid: #5e5e5e;
    --panel: rgba(150,150,150,0.35);
    --panel-edge: rgba(255,255,255,0.08);
    --info-box: rgba(120,120,120,0.75);
    --yellow: #f5ee12;
    --red: #e8101a;
    --green: #12e84a;
    --white: #ffffff;
    --cyan: #12e6f0;
    --arrow: rgba(170,170,170,0.55);
    --glow: #7a2a2e;
  }
  * { margin: 0; padding: 0; box-sizing: border-box; }
  html, body { width: 1200px; height: 900px; overflow: hidden; }
  body { background: var(--bg-edge); }

  .poster {
    position: relative;
    width: 1200px;
    height: 900px;
    overflow: hidden;
    background: radial-gradient(ellipse at 60% 40%, var(--bg-mid) 0%, #3e3e3e 55%, var(--bg-edge) 100%);
  }

  .slogan-panel {
    position: absolute;
    left: 206px; top: 25px;
    width: 975px; height: 611px;
    border-radius: 12px;
    background: linear-gradient(180deg, rgba(170,170,170,0.45), rgba(120,120,120,0.35));
    border: 1px solid var(--panel-edge);
  }

  .ghost-photo {
    position: absolute;
    left: 560px; top: 25px;
    width: 560px; height: 611px;
    background: radial-gradient(ellipse at 55% 35%, rgba(200,200,200,0.25), rgba(120,120,120,0.05) 70%);
    border-radius: 12px;
  }

  .speaker-photo {
    position: absolute;
    left: 790px; top: 250px;
    width: 410px; height: 650px;
    background:
      radial-gradient(ellipse at 40% 45%, rgba(230,230,230,0.85) 0%, rgba(140,140,140,0.7) 35%, rgba(122,42,46,0.55) 65%, rgba(122,42,46,0) 100%);
  }

  .lockout-tag {
    position: absolute;
    left: 808px; top: 615px;
    width: 100px; height: 280px;
    border-radius: 14px 14px 6px 6px;
    background: linear-gradient(180deg, #c01818, #8e0d10);
  }

  .slogan {
    position: absolute;
    left: 245px;
    font-family: "Anton", Impact, sans-serif;
    font-style: italic;
    transform: skewX(-8deg);
    transform-origin: left;
    line-height: 1.1;
  }
  .slogan--warning { top: 118px; color: var(--yellow); font-size: 37px; }
  .slogan--warning .initial { font-size: 88px; line-height: 0.8; vertical-align: -4px; }
  .slogan--warning .line2 { display: block; margin-top: -4px; }
  .slogan--alert { top: 282px; color: var(--red); font-size: 44px; line-height: 1.2; }
  .slogan--call { top: 452px; color: var(--green); font-size: 38px; line-height: 1.4; }

  .booking-box {
    position: absolute;
    left: 20px; top: 655px;
    width: 540px; height: 250px;
    background: var(--info-box);
    border-radius: 2px;
  }
  .booking-title {
    position: absolute;
    left: 14px; top: 18px;
    font-family: "Roboto Condensed", Arial, sans-serif;
    font-style: italic;
    font-weight: 800;
    font-size: 40px;
    line-height: 1.3;
    color: var(--white);
  }
  .booking-title .speaker-name { color: var(--cyan); }
  .booking-contact {
    position: absolute;
    right: 22px; top: 142px;
    text-align: right;
    font-family: "Roboto Condensed", Arial, sans-serif;
    font-style: italic;
    font-weight: 800;
    font-size: 34px;
    line-height: 1.35;
    color: var(--white);
  }

  .pointer-arrow { position: absolute; left: 568px; top: 715px; }
</style>
</head>
<body>
  <main class="poster">
    <div class="slogan-panel"></div>
    <div class="ghost-photo" role="img" aria-label="Faded enlarged black and white portrait of the speaker"></div>
    <div class="speaker-photo" role="img" aria-label="Black and white photo of the speaker wearing a prosthetic arm, with a red glow behind her"></div>
    <div class="lockout-tag" role="img" aria-label="Red danger do not operate lockout tag held in the prosthetic hook"></div>

    <p class="slogan slogan--warning"><span class="initial">Y</span>ou don’t know what will<span class="line2">happen one second letter....</span></p>
    <p class="slogan slogan--alert">If you don’t think it will<br>happen to you...<br>think again</p>
    <p class="slogan slogan--call">Choose safety<br>Keep alert is the best way.</p>

    <section class="booking-box">
      <h2 class="booking-title">Book a Safety Presentation<br>with <span class="speaker-name">Dara Voss</span></h2>
      <p class="booking-contact">612-555-0487<br>www.daravossmail.net</p>
    </section>

    <svg class="pointer-arrow" width="180" height="120" viewBox="0 0 180 120" aria-hidden="true">
      <polygon points="0,30 88,30 88,0 178,60 88,120 88,92 0,92" fill="var(--arrow)"/>
    </svg>
  </main>
</body>
</html>
```